Brellhaven.co.uk Double Sided A4 Folder needs designing
Brellhaven.co.uk needs a folder design
Hi
Thanks you so much for the great designs, we prefer more blue than gold, some of the designs have way to much gold..
Owen
Thank you so much Tobrik ...
nice work @ KorvenDale :)
@Project Holder.
Need your feedback please.
Thanks
KorvenDale
We deal with properties in the mayfair area, you can view the mayfair website to get an idea of the area.
http://www.ostrelwick-area.co.uk/
The title could be 'Your Mayfair Estate Agents'
the look of the folder should have our color blue and gold, ie royal blue and gold design, it should look almost like it is a royal invitation..
examples of some ideas of the design you can get some inspiration below
http://www.prindova.co.uk/royal_blue_and_gold_monogram_wedding_invitation-274819305527183940
http://www.snapvelo.com/photos/inkmarble/5830416297/
http://img.prindovacdn.com/royal_blue_and_gold_floral_envelope_fits_5x7_sizes-p48301927455061273914eg6_325.jpg?t_image1_iid=AB4C1937-2210-4F7E-B913-50DA7E2C18A6&t_text1=Marla%20Quint%0D%0A517%20Ferncroft%20Lane%0D%0AHolvale%2C%20NY%2067890
Our address is as below
Brell Haven
14b Pellam Row
Mayfair
London
W9X 4QF
Dear PH,
Don't you think, an address or any contact info/tagline would be appropriate to be placed on the folder.
Could you give more details on your business (what kind of properties do you deal with/ May be necessary in case of use of images

```html
<!DOCTYPE html>
<html lang="en">
<head>
<meta charset="utf-8">
<title>Brell Haven Folder</title>
<link rel="stylesheet" href="https://fonts.googleapis.com/css2?family=Cinzel:wght@600&family=Open+Sans:wght@400;600;700&display=swap">
<style>
  :root {
    --backdrop: #111111;
    --gold-light: #f3d76a;
    --gold: #d8b33e;
    --gold-deep: #b58f22;
    --royal: #1f3a94;
    --royal-dark: #15296f;
    --royal-soft: #3a58b4;
    --white: #ffffff;
  }
  html, body {
    margin: 0;
    padding: 0;
    width: 1200px;
    height: 950px;
    overflow: hidden;
    background: var(--backdrop);
  }
  .canvas {
    position: relative;
    width: 1200px;
    height: 950px;
  }
  .folder-spread {
    position: absolute;
    left: 70px;
    top: 110px;
    width: 1060px;
    height: 730px;
    display: flex;
    box-shadow: 0 10px 40px rgba(0,0,0,.6);
  }
  .panel-back {
    position: relative;
    width: 530px;
    height: 730px;
    background: radial-gradient(circle at 50% 48%, var(--gold-light) 0%, var(--gold) 55%, var(--gold-deep) 100%);
  }
  .back-brand {
    position: absolute;
    left: 0;
    right: 0;
    top: 300px;
    text-align: center;
  }
  .brand-dot {
    display: block;
    margin: 0 auto 14px;
    width: 58px;
    height: 58px;
    border-radius: 50%;
    background: var(--royal);
  }
  .brand-name {
    font-family: "Cinzel", serif;
    font-weight: 600;
    font-size: 20px;
    letter-spacing: 4px;
    color: var(--royal);
  }
  .brand-tagline {
    margin-top: 4px;
    font-family: "Open Sans", sans-serif;
    font-size: 9px;
    letter-spacing: 2px;
    color: var(--royal);
  }
  .panel-front {
    position: relative;
    width: 530px;
    height: 730px;
    overflow: hidden;
  }
  .panel-front svg {
    position: absolute;
    inset: 0;
  }
  .title-band {
    position: absolute;
    left: 0;
    top: 250px;
    width: 330px;
    padding: 12px 0 12px 22px;
    background: var(--royal-dark);
    font-family: "Open Sans", sans-serif;
    color: var(--white);
  }
  .title-line {
    font-size: 24px;
    line-height: 1.1;
  }
  .title-place {
    font-weight: 700;
    font-size: 40px;
    color: var(--gold-light);
    letter-spacing: 1px;
  }
  .front-brand {
    position: absolute;
    right: 28px;
    bottom: 40px;
    text-align: center;
  }
  .front-brand .brand-dot {
    width: 42px;
    height: 42px;
    margin-bottom: 8px;
  }
  .front-brand .brand-name {
    font-size: 14px;
    letter-spacing: 3px;
  }
</style>
</head>
<body>
<main class="canvas">
  <section class="folder-spread">
    <div class="panel-back">
      <div class="back-brand">
        <span class="brand-dot"></span>
        <div class="brand-name">BRELL HAVEN</div>
        <div class="brand-tagline">LUXURY HOMES IN MAYFAIR</div>
      </div>
    </div>
    <div class="panel-front">
      <svg width="530" height="730" viewBox="0 0 530 730" aria-hidden="true">
        <rect width="530" height="730" fill="var(--royal)"/>
        <g fill="none" stroke="var(--royal-soft)" stroke-opacity=".55">
          <circle cx="560" cy="170" r="430" stroke-width="40"/>
          <circle cx="560" cy="170" r="340" stroke-width="30"/>
          <circle cx="560" cy="170" r="260" stroke-width="22"/>
        </g>
        <path d="M530,150 C420,330 380,560 170,730 L530,730 Z" fill="var(--white)"/>
        <path d="M530,150 C420,330 380,560 170,730" fill="none" stroke="var(--gold)" stroke-width="8"/>
      </svg>
      <div class="title-band">
        <div class="title-line">Your <span class="title-place">MAYFAIR</span></div>
        <div class="title-line">Estate Agents</div>
      </div>
      <div class="front-brand">
        <span class="brand-dot"></span>
        <div class="brand-name">BRELL HAVEN</div>
      </div>
    </div>
  </section>
</main>
</body>
</html>
```